Looking for awesome business card design with attached existing logo

We are a water, mold, and fire damage restoration company called "Falcon Shield" Looking for an awesome business card that is edgy yet professional and unique. Show me what you got!

```html
<!DOCTYPE html>
<html lang="en">
<head>
<meta charset="utf-8">
<title>Falcon Shield – Business Card</title>
<link rel="stylesheet" href="https://fonts.googleapis.com/css2?family=Arimo:wght@400;700&display=swap">
<style>
  :root {
    --backdrop: #e4e4e2;
    --card: #2f4b58;
    --gold: #d39a1e;
    --edge: #c08a1a;
    --ink: #ffffff;
    --rule: #9fb0b8;
  }
  * { box-sizing: border-box; margin: 0; padding: 0; }
  html, body { width: 1200px; height: 802px; overflow: hidden; }
  body {
    background: var(--backdrop);
    font-family: "Arimo", Arial, sans-serif;
    position: relative;
  }
  .card {
    position: absolute;
    top: 246px;
    width: 540px;
    height: 310px;
    background: var(--card);
    border-bottom: 3px solid var(--edge);
    border-right: 2px solid var(--edge);
    box-shadow: 0 10px 24px rgba(0,0,0,0.18);
  }
  .card--front { left: 40px; }
  .card--back { left: 620px; }

  .brand {
    display: flex;
    align-items: center;
    gap: 10px;
    color: var(--ink);
    font-weight: 700;
    letter-spacing: 0.5px;
  }
  .brand__dot {
    width: 12px; height: 12px;
    border-radius: 50%;
    background: var(--gold);
    flex: none;
  }
  .card--front .brand {
    position: absolute;
    left: 40px;
    top: 138px;
    font-size: 27px;
  }
  .divider {
    position: absolute;
    left: 272px;
    top: 64px;
    width: 1px;
    height: 182px;
    background: var(--rule);
  }
  .contact {
    position: absolute;
    left: 296px;
    top: 68px;
    color: var(--ink);
    font-size: 14px;
    line-height: 1.35;
  }
  .contact__name {
    color: var(--gold);
    font-weight: 700;
    font-size: 17px;
    letter-spacing: 0.3px;
  }
  .contact__role { margin-bottom: 12px; }
  .contact__address { margin-bottom: 14px; }
  .contact__line {
    display: flex;
    align-items: center;
    gap: 8px;
    margin-bottom: 3px;
  }
  .contact__icon { width: 13px; height: 13px; flex: none; }

  .card--back .brand {
    position: absolute;
    left: 50%;
    top: 50%;
    transform: translate(-50%, -50%);
    font-size: 40px;
    gap: 14px;
  }
  .card--back .brand__dot { width: 16px; height: 16px; }
</style>
</head>
<body>
  <section class="card card--front">
    <div class="brand"><span class="brand__dot"></span>Falcon Shield</div>
    <div class="divider"></div>
    <div class="contact">
      <p class="contact__name">MARCUS REYES</p>
      <p class="contact__role">Manager</p>
      <p class="contact__address">Your Address, City<br>State, Zip 0000</p>
      <p class="contact__line">
        <svg class="contact__icon" viewBox="0 0 16 16" aria-hidden="true"><circle cx="8" cy="8" r="8" fill="var(--gold)"/><path d="M5 4.5l1.6-.4.9 2-1 .8a5 5 0 0 0 2.6 2.6l.8-1 2 .9-.4 1.6c-3.6.2-6.7-2.9-6.5-6.5z" fill="var(--card)"/></svg>
        123-456-2100
      </p>
      <p class="contact__line">
        <svg class="contact__icon" viewBox="0 0 16 16" aria-hidden="true"><rect x="1" y="3.5" width="14" height="9" fill="var(--gold)"/><path d="M1.5 4l6.5 5 6.5-5" fill="none" stroke="var(--card)" stroke-width="1.2"/></svg>
        hello@falconshield.co
      </p>
      <p class="contact__line">
        <svg class="contact__icon" viewBox="0 0 16 16" aria-hidden="true"><circle cx="8" cy="8" r="8" fill="var(--gold)"/><ellipse cx="8" cy="8" rx="3" ry="6" fill="none" stroke="var(--card)" stroke-width="1"/><path d="M2 8h12" stroke="var(--card)" stroke-width="1"/></svg>
        www.falconshield.co
      </p>
    </div>
  </section>

  <section class="card card--back">
    <div class="brand"><span class="brand__dot"></span>Falcon Shield</div>
  </section>
</body>
</html>
```